Law firm for traffic law - company portfolio

Company folder with logo and picture on the front. On the back only the imprint in DinA4 format. The following folders are ordered
https://www.falzhaus-kremvel.de/mappe-fuer-din-a4-2teilig-mit-2-laschen-40-farbig-aussseite-bedruck-mit-mattfolie-kaschiert.html#content-view

```html
<!DOCTYPE html>
<html lang="de">
<head>
<meta charset="utf-8">
<title>LEXVIA – Unternehmensmappe</title>
<link rel="stylesheet" href="https://fonts.googleapis.com/css2?family=Montserrat:wght@400;600;700;800&display=swap">
<style>
  :root{
    --navy:#1f3a5a;
    --navy-dark:#162c46;
    --orange:#f0a024;
    --amber:#f6c02e;
    --paper:#ffffff;
    --flap:#d9dcdf;
    --stage:#eceef0;
    --text-grey:#6b7380;
    --photo-a:#9a6a5a;
    --photo-b:#a92b2b;
    --photo-c:#5b6470;
  }
  *{box-sizing:border-box;margin:0;padding:0}
  html,body{width:813px;height:1200px;overflow:hidden}
  body{background:var(--stage);font-family:"Montserrat",sans-serif;position:relative}
  .dieline{position:absolute;left:0;top:0}
  .brand{position:absolute;font-weight:800;letter-spacing:2px;font-size:24px;line-height:1;color:var(--navy);display:flex;flex-direction:column;align-items:flex-start}
  .brand small{font-size:7px;font-weight:600;letter-spacing:1.6px;line-height:1;color:var(--text-grey);margin-top:3px}
  .brand--back{left:120px;top:262px}
  .brand--front{left:470px;top:262px}
  .brand--light{color:var(--paper);font-size:26px;align-items:center}
  .brand--light small{color:#c9d3df}
  .brand--back-pocket{left:171px;top:644px}
  .brand--front-pocket{left:501px;top:644px}
  .photo{position:absolute;left:424px;top:326px;width:294px;height:172px;
    background:linear-gradient(160deg,var(--photo-c) 0%,var(--photo-a) 45%,var(--photo-b) 100%)}
  .chain-art{position:absolute;left:96px;top:326px;width:290px;height:190px;
    background:radial-gradient(ellipse at center,#d9dde2 0%,#eef0f2 60%,#fff 100%)}
  .headline{position:absolute;left:424px;top:510px;font-weight:700;line-height:1.05}
  .headline .lead{color:var(--orange);font-size:19px;display:block}
  .headline .sub{color:var(--navy);font-size:19px;display:block}
  .contact{position:absolute;left:96px;top:560px;width:290px;display:flex;justify-content:space-between;font-size:8.5px;color:var(--text-grey);font-weight:600}
  .contact-item{display:flex;align-items:center;gap:4px}
  .contact-item svg{flex:none}
</style>
</head>
<body>
<svg class="dieline" width="813" height="1200" viewBox="0 0 813 1200" xmlns="http://www.w3.org/2000/svg">
  <path d="M76 280 L40 300 L40 690 L76 710 Z" fill="var(--flap)"/>
  <path d="M736 280 L772 300 L772 690 L736 710 Z" fill="var(--flap)"/>
  <path d="M76 710 L396 710 L396 850 Q396 870 376 870 L100 870 Q76 870 76 846 Z" fill="var(--flap)"/>
  <path d="M416 710 L736 710 L736 846 Q736 870 712 870 L436 870 Q416 870 416 850 Z" fill="var(--flap)"/>
  <rect x="396" y="710" width="20" height="60" fill="var(--flap)"/>
  <rect x="76" y="240" width="660" height="470" fill="var(--paper)"/>
  <path d="M76 610 L300 610 L330 596 L406 596 L406 710 L76 710 Z" fill="var(--navy)"/>
  <path d="M406 596 L630 596 L660 610 L736 610 L736 710 L406 710 Z" fill="var(--navy)"/>
  <line x1="406" y1="240" x2="406" y2="710" stroke="#e4e6e8" stroke-width="1"/>
  <path d="M352 240 L460 240 L430 300 L406 258 L382 300 Z" fill="var(--amber)"/>
  <path d="M382 300 L406 258 L430 300 Z" fill="var(--orange)"/>
  <path d="M392 300 L406 276 L420 300 Z" fill="var(--navy)"/>
  <path d="M220 300 L352 300 L344 312 L212 312 Z" fill="var(--navy)"/>
  <path d="M600 300 L736 300 L736 312 L592 312 Z" fill="var(--navy)"/>
  <path d="M90 300 L212 300 L208 306 L86 306 Z" fill="var(--orange)"/>
  <path d="M460 300 L592 300 L588 306 L456 306 Z" fill="var(--orange)"/>
</svg>

<div class="brand brand--back">LEXVIA<small>VERKEHRSRECHT KANZLEI</small></div>
<div class="brand brand--front">LEXVIA<small>VERKEHRSRECHT KANZLEI</small></div>

<div class="chain-art" role="img" aria-label="Blasse Hintergrundgrafik einer Kette"></div>

<div class="contact">
  <span class="contact-item">
    <svg width="10" height="10" viewBox="0 0 10 10"><circle cx="5" cy="5" r="5" fill="var(--orange)"/><path d="M3 2.5 L4.3 2.5 L4.8 4 L4 4.6 Q4.8 5.8 5.5 6 L6.1 5.2 L7.5 5.7 L7.5 7 Q4 7.4 3 3.5 Z" fill="#fff"/></svg>
    06 123 4 56 78 90
  </span>
  <span class="contact-item">
    <svg width="10" height="10" viewBox="0 0 10 10"><circle cx="5" cy="5" r="5" fill="var(--orange)"/><rect x="2.5" y="3.2" width="5" height="3.6" fill="#fff"/><path d="M2.5 3.2 L5 5 L7.5 3.2" stroke="var(--orange)" stroke-width=".6" fill="none"/></svg>
    info@lexvia.de
  </span>
  <span class="contact-item">
    <svg width="10" height="10" viewBox="0 0 10 10"><circle cx="5" cy="5" r="5" fill="var(--orange)"/><circle cx="5" cy="5" r="2.6" fill="none" stroke="#fff" stroke-width=".8"/><line x1="2.4" y1="5" x2="7.6" y2="5" stroke="#fff" stroke-width=".7"/></svg>
    www.lexvia.de
  </span>
</div>

<div class="photo" role="img" aria-label="Foto einer Person, die nach einem Unfall an einem roten Auto sitzt"></div>

<h1 class="headline"><span class="lead">PROFESSIONELLES</span><span class="sub">UNFALL-</span><span class="sub">MANAGEMENT</span></h1>

<div class="brand brand--light brand--back-pocket">LEXVIA<small>VERKEHRSRECHT KANZLEI</small></div>
<div class="brand brand--light brand--front-pocket">LEXVIA<small>VERKEHRSRECHT KANZLEI</small></div>
</body>
</html>
```